Consulting Firm stationery design

Now that the ArtHive has given us a new logo we'll now need to have all our stationery designed. So we're asking for this community to help us once again.We're looking to get from you Letterheads (Header and Footer, suitable to be applied on a .docx format. Vectors are required but keep this in mind), Envelopes (Front and Back designs, back is not a must but desirable depending on your design), 9"x 12" Pocket Folders (consider design for front and back, also for pockets as well), Business Cards.An elegant design is a must have, mostly for Folders and Envelopes. The idea with this two is to stand out from others when they're handed over. Ideas are welcomed, we were thinking maybe on some texturing simulation for these.Folders will have 3 addresses and contact information. Envelopes will have 1 address and contact information.Brand Manual attached. marquesino logo has been copyrighted already. I'm also attaching the current stationary designs (these never got to be out for production but was going to be before we made the brand changes); Pocker folders page 1 to 4 (pages 2 and 4 are the pocket designs), Pages 5 and 6 (6 is the back of the envelope), Pages 7 and 8 (8 is the back of the business card). No letterhead within these designs as it just had the logo and address.

Industry/Entity Type

Business Consultant

Font styles to use
Serif
Sans Serif

Requirements
Must have
• Elegance
Nice to have
• Modern looking out of common

```html
<!DOCTYPE html>
<html lang="en">
<head>
<meta charset="utf-8">
<title>marquesino — Pocket Folder</title>
<link rel="stylesheet" href="https://fonts.googleapis.com/css2?family=Poppins:wght@500&family=Roboto:wght@400;700&display=swap">
<style>
  :root {
    --brand-blue: #3f82c8;
    --brand-blue-deep: #2f6fb4;
    --brand-blue-light: #5a96d4;
    --ink: #2b2b2b;
    --band: #2a2a2a;
    --paper: #ffffff;
    --paper-shade: #f1f1f1;
    --canvas: #e4e4e4;
    --white: #ffffff;
  }
  * { box-sizing: border-box; margin: 0; padding: 0; }
  html, body { width: 842px; height: 1200px; overflow: hidden; }
  body {
    background: var(--canvas);
    font-family: "Roboto", Arial, sans-serif;
    position: relative;
  }
  .spread {
    position: absolute;
    left: 51px;
    width: 740px;
    height: 493px;
    display: flex;
    box-shadow: 0 6px 18px rgba(0,0,0,0.18);
  }
  .spread--outside { top: 60px; }
  .spread--inside { top: 620px; }
  .panel { position: relative; width: 370px; height: 493px; overflow: hidden; }

  /* Back cover */
  .back-cover {
    background: linear-gradient(160deg, var(--brand-blue-light) 0%, var(--brand-blue) 45%, var(--brand-blue-deep) 100%);
    color: var(--white);
  }
  .partner-band {
    position: absolute; left: 0; top: 170px; width: 100%; height: 66px;
    background: var(--band);
    display: flex; align-items: center; justify-content: space-around;
    padding: 0 30px;
  }
  .partner-badge { width: 62px; height: 20px; border-radius: 3px; background: rgba(255,255,255,0.85); }
  .partner-badge--small { width: 44px; }
  .back-footer { position: absolute; left: 28px; right: 28px; bottom: 26px; }
  .footer-rule { height: 1px; background: rgba(255,255,255,0.5); margin-bottom: 12px; }
  .brand-mini { display: flex; align-items: center; gap: 4px; font-family: "Poppins", sans-serif; font-weight: 500; font-size: 15px; margin-bottom: 4px; }
  .brand-mini .dot { width: 8px; height: 8px; border-radius: 50%; background: var(--white); }
  .contact-list { list-style: none; font-size: 6.5px; line-height: 1.5; margin-bottom: 8px; }
  .contact-list li { display: flex; align-items: center; gap: 4px; }
  .contact-list svg { width: 6px; height: 6px; fill: var(--white); }
  .address-row { display: flex; gap: 14px; border-top: 1px solid rgba(255,255,255,0.5); padding-top: 7px; }
  .address { font-size: 6.5px; line-height: 1.45; flex: 1; }
  .address strong { display: block; font-weight: 700; }

  /* Front cover */
  .front-cover { background: linear-gradient(135deg, var(--paper) 40%, var(--paper-shade) 100%); }
  .brand-mark {
    position: absolute; left: 0; right: 0; top: 110px;
    display: flex; align-items: center; justify-content: center; gap: 8px;
    font-family: "Poppins", sans-serif; font-weight: 500; font-size: 46px;
    color: var(--ink); letter-spacing: -0.5px;
  }
  .brand-mark .dot { width: 20px; height: 20px; border-radius: 50%; background: var(--brand-blue); }
  .edge-strip { position: absolute; bottom: 0; height: 8px; }
  .edge-strip--blue { left: 0; width: 62%; background: var(--brand-blue); }
  .edge-strip--dark { right: 0; width: 38%; background: var(--band); }

  /* Inside */
  .inside-panel { background: linear-gradient(180deg, var(--paper) 0%, var(--paper-shade) 100%); }
  .inside-panel + .inside-panel { border-left: 1px solid #dcdcdc; }
  .pocket { position: absolute; left: 0; bottom: 0; width: 370px; height: 190px; }
</style>
</head>
<body>

<section class="spread spread--outside" aria-label="Folder outside">
  <div class="panel back-cover">
    <div class="partner-band">
      <span class="partner-badge"></span>
      <span class="partner-badge"></span>
      <span class="partner-badge partner-badge--small"></span>
    </div>
    <div class="back-footer">
      <div class="footer-rule"></div>
      <div class="brand-mini">marquesino<span class="dot"></span></div>
      <ul class="contact-list">
        <li><svg viewBox="0 0 10 10"><path d="M2 0h2l1 3-1.5 1a6 6 0 0 0 2.5 2.5L7 5l3 1v2a2 2 0 0 1-2 2A8 8 0 0 1 0 2a2 2 0 0 1 2-2z"/></svg>(809) 555-0142</li>
        <li><svg viewBox="0 0 10 10"><path d="M0 2h10v6H0z M0 2l5 3 5-3"/></svg>hola@marquesino.do</li>
        <li><svg viewBox="0 0 10 10"><circle cx="5" cy="5" r="5"/></svg>www.marquesino.do</li>
      </ul>
      <div class="address-row">
        <p class="address"><strong>Administration Office</strong>Torre Alameda, Calle Los Robles 42, Naco, Santo Domingo, Rep. Dominicana</p>
        <p class="address"><strong>Ventas Globales</strong>418 Harbor View Road, Suite 7, Dover, Delaware 19901, United States</p>
        <p class="address"><strong>Operations</strong>Edificio Cumbre, Av. Las Palmas 15, Santo Domingo, Rep. Dominicana</p>
      </div>
    </div>
  </div>
  <div class="panel front-cover">
    <div class="brand-mark">marquesino<span class="dot"></span></div>
    <span class="edge-strip edge-strip--blue"></span>
    <span class="edge-strip edge-strip--dark"></span>
  </div>
</section>

<section class="spread spread--inside" aria-label="Folder inside with pockets">
  <div class="panel inside-panel">
    <svg class="pocket" viewBox="0 0 370 190" aria-hidden="true">
      <defs>
        <linearGradient id="pocketFill" x1="0" y1="0" x2="1" y2="1">
          <stop offset="0" stop-color="#5a96d4"/>
          <stop offset="1" stop-color="#3f82c8"/>
        </linearGradient>
      </defs>
      <polygon points="0,0 300,0 370,40 370,190 0,190" fill="url(#pocketFill)"/>
    </svg>
  </div>
  <div class="panel inside-panel">
    <svg class="pocket" viewBox="0 0 370 190" aria-hidden="true">
      <polygon points="0,40 70,0 370,0 370,190 0,190" fill="url(#pocketFill)"/>
    </svg>
  </div>
</section>

</body>
</html>
```